Website for residential builder repair in Australia

I currently have my website setup using Servolink as hosting and started playing around with Wordpress.
I would like this to be able to be imported into Wordpress after built so I can add blog posts and edit site if needed.

I would like a website built that is simple and clear.

the main colours id like for the site are black and white and maybe grey.

I would like a simple welcome page, an about us page, a project page, and a blog page where I can write small articles.

will need to display licence number on website lic. 731046K

Target Market(s)

young to middle age families and couples looking to build a sustainable and high performance house.

Contact Information for Business Card

Tamsel Construction
Lic. 731046K (to be printed small)
email; bram@tamselconstruction.com.au
phone : 0428159067

Bram Keltoy - Director

Number of Pages Required

4 page

Font styles to use
Sans Serif
Other font styles liked:
• match logo

Colors

Designer to choose only greyscale colors for use in the design.

Requirements
Must have
• outline of works

Certified Passive House Tradesperson
New Builds
Renovations
Architectural homes
Nice to have
• thinking dark grey background or black

would like to see the logo embossed to look slightly 3d

back of card to be white or light grey so It can be written on.

letterhead to contain licence number swell

```html
<!DOCTYPE html>
<html lang="en">
<head>
<meta charset="utf-8">
<title>Tamsel Construction – Business Card</title>
<link rel="stylesheet" href="https://fonts.googleapis.com/css2?family=Jost:wght@300;400;700&display=swap">
<style>
  :root {
    --card-dark: #353535;
    --card-light: #f0f0ee;
    --brand-white: #f4f4f4;
    --licence-grey: #a9a9a9;
    --ink: #1c1c1c;
    --role-grey: #8a8a8a;
    --accent: #d4dc2a;
  }
  * { box-sizing: border-box; margin: 0; padding: 0; }
  html, body {
    width: 1200px;
    height: 686px;
    overflow: hidden;
    background: var(--card-light);
  }
  .card {
    position: relative;
    width: 1200px;
    height: 686px;
    font-family: "Jost", "Futura", sans-serif;
  }
  .brand-panel {
    position: absolute;
    left: 0; top: 0;
    width: 1200px;
    height: 425px;
    background: var(--card-dark);
  }
  .brand-name {
    position: absolute;
    left: 0; top: 108px;
    width: 1200px;
    text-align: center;
    color: var(--brand-white);
    font-weight: 300;
    font-size: 104px;
    line-height: 1;
    letter-spacing: 30px;
    text-indent: 30px;
  }
  .brand-sub {
    position: absolute;
    left: 0; top: 232px;
    width: 1200px;
    text-align: center;
    color: var(--brand-white);
    font-weight: 300;
    font-size: 33px;
    line-height: 1;
    letter-spacing: 24px;
    text-indent: 24px;
  }
  .licence {
    position: absolute;
    left: 0; top: 293px;
    width: 1200px;
    text-align: center;
    color: var(--licence-grey);
    font-weight: 300;
    font-size: 20px;
    letter-spacing: 2px;
  }
  .contact-panel {
    position: absolute;
    left: 0; top: 425px;
    width: 1200px;
    height: 261px;
    background: var(--card-light);
  }
  .accent-bar {
    position: absolute;
    left: 3px; top: 47px;
    width: 25px;
    height: 166px;
    background: var(--accent);
  }
  .person-name {
    position: absolute;
    left: 54px; top: 72px;
    color: var(--ink);
    font-weight: 300;
    font-size: 62px;
    line-height: 1;
  }
  .person-role {
    position: absolute;
    left: 55px; top: 150px;
    color: var(--role-grey);
    font-weight: 700;
    font-size: 31px;
    line-height: 1;
    letter-spacing: 1.5px;
  }
  .contact-details {
    position: absolute;
    right: 48px; top: 70px;
    text-align: right;
    color: var(--ink);
    font-weight: 300;
    font-size: 46px;
    line-height: 70px;
  }
</style>
</head>
<body>
  <div class="card">
    <section class="brand-panel">
      <div class="brand-name">TAMSEL</div>
      <div class="brand-sub">CONSTRUCTION</div>
      <div class="licence">Lic. 731046K</div>
    </section>
    <section class="contact-panel">
      <div class="accent-bar"></div>
      <div class="person-name">Bram Keltoy</div>
      <div class="person-role">Director</div>
      <div class="contact-details">
        <div class="email">bram@tamselconstruction.com.au</div>
        <div class="phone">0428159067</div>
      </div>
    </section>
  </div>
</body>
</html>
```